Commercial Janitorial Company needs a Postcard Design

We need a postcard design-i attached a sample-of one-not our industry-but same size and similar to content and what i am looking for-We are a commercial janitorial service-(not residential) we service High Tech-Bio Tech-Manufacturing-Office-Property Management Company'sThe design should incorporate Industry Services-Industries served website-company information-Two sided-color-our website: www.marlowcrestfacilitysvc.com will have information to use-bullet point type-should include Nice artwork-Attention grabbing headline then of course all our contact information found on website

The postcard is NOT a mailer but a hand-out (2 sides)-about 9" Long by 7" wide-

Target Market(s)

Commercial office Building's

Colors

Designer to choose colors to be used in the design.

Requirements
Must have
• All company information-website
• Services offered-Industries served
• Something mentioned about "Green Cleaning"
• Images of cleaning are good-in a commercial setting--Hi Tech-Bio Tech-Cleanroom Cleaning
• 24/7 access
• Locally owned and operated
• 25 Years in business
• Service Excellence
• With our highly-trained, in-house workforce, you can trust that we’ll provide you with services that increase efficiencies and lower your operating expenses—all while maintaining a uniform standard of service excellence.
• Breadth of Services
• We’ll provide you with an unrivaled range of facilities solutions that will keep your properties safe, clean, comfortable and energy efficient.
• Technology-Enabled Workforce
• Your facilities will be serviced with the support of innovative technology solutions that will simplify service delivery and allow for greater transparency.
• Guaranteed Sustainability Solutions
• We’ve got expertise to support all of your sustainability goals, including green cleaning, VORQ support, bundled energy solutions, and more.
• Size of Postcard is 9.5" length x 7" width
Should not have
• No Residential
• No Maid service
• No Cartoon type images
• Strickly commercial cleaning

```html
<!DOCTYPE html>
<html lang="en">
<head>
<meta charset="utf-8">
<title>Commercial Janitorial Service – Two-Sided Hand-out</title>
<link href="https://fonts.googleapis.com/css2?family=Lato:ital,wght@0,400;0,700;0,900;1,400&display=swap" rel="stylesheet">
<style>
:root{
  --green:#1f9a3a;
  --green-dark:#167a2c;
  --blue:#1a73c2;
  --blue-dark:#0f5c9e;
  --ink:#2a2a2a;
  --muted:#4a4a4a;
  --paper:#ffffff;
  --stage:#eef0f2;
}
*{box-sizing:border-box;margin:0;padding:0}
html,body{width:1200px;height:1200px;overflow:hidden;background:var(--stage);font-family:"Lato",sans-serif;color:var(--ink)}
.sheet{position:absolute;top:236px;width:540px;height:728px;background:var(--paper);overflow:hidden;box-shadow:0 6px 18px rgba(0,0,0,.18)}
.sheet--front{left:40px}
.sheet--back{left:620px}
.backdrop{position:absolute;inset:0}
.photo{position:absolute}
.photo--hero{left:0;top:0;width:540px;height:250px;background:linear-gradient(135deg,#3d5d80 0%,#8ea6bf 45%,#c9d4de 70%,#6d7f92 100%)}
.photo--cleanroom{left:0;top:0;width:540px;height:215px;background:linear-gradient(180deg,#b9c4cc 0%,#e1e6ea 45%,#8e9ba6 100%)}
.photo--round{border-radius:50%;border:4px solid #fff;box-shadow:0 2px 6px rgba(0,0,0,.25)}
.title-block{position:absolute;left:28px;top:288px;color:#fff}
.title-block .kicker{font-weight:900;font-size:17px;letter-spacing:.3px}
.title-block h1{font-weight:900;font-size:27px;letter-spacing:.3px;line-height:1.05}
.title-block p{font-size:13px;line-height:1.2;margin-top:4px}
.col{position:absolute;font-size:8.6px;line-height:1.3;color:var(--muted)}
.col p{margin-bottom:6px;text-align:justify}
.h-section{color:var(--blue);font-weight:900;font-size:13.5px;margin-bottom:5px}
.h-sub{color:var(--green);font-weight:700;font-size:10.5px;margin:6px 0 3px}
.lead-in{color:var(--blue);font-style:italic;font-size:8.4px;margin-bottom:4px}
.checks{list-style:none}
.checks li{position:relative;padding-left:12px;margin-bottom:5px;color:var(--ink)}
.checks li::before{content:"";position:absolute;left:1px;top:1px;width:4px;height:7px;border:solid var(--ink);border-width:0 1.6px 1.6px 0;transform:rotate(40deg)}
.checks--two{display:grid;grid-template-columns:1fr 1fr;column-gap:6px}
.features{display:flex;gap:8px;margin-top:6px}
.feature{width:56px;text-align:center;font-size:8.6px;color:var(--ink);line-height:1.2}
.feature .icon{width:36px;height:36px;border-radius:50%;background:var(--blue);margin:0 auto 5px;display:flex;align-items:center;justify-content:center;box-shadow:0 0 0 3px #d6e6f5}
.cta{color:var(--blue);font-size:9.5px;line-height:1.2}
.phone{display:inline-block;margin-top:6px;background:var(--green);color:#fff;font-weight:900;font-size:14px;padding:4px 12px;border-radius:14px;border:2px solid #cfe9d5}
.brand{display:flex;align-items:center;gap:6px}
.brand .mark{width:22px;height:22px;background:var(--blue-dark)}
.brand .name{color:var(--blue);font-weight:900;font-size:15px;line-height:1}
.footer{position:absolute;left:0;bottom:0;width:100%;height:46px;background:var(--blue);color:#fff;font-size:10px;display:flex;align-items:center;justify-content:space-between;padding:0 28px}
.footer span{display:flex;align-items:center;gap:5px}
.dot{width:8px;height:8px;border-radius:50%;background:#fff;display:inline-block}
</style>
</head>
<body>

<section class="sheet sheet--front">
  <div class="photo photo--hero" role="img" aria-label="Floor burnisher and yellow wet-floor caution sign on a polished commercial floor"></div>
  <svg class="backdrop" viewBox="0 0 540 728" aria-hidden="true">
    <path d="M0,420 C180,405 360,390 540,372 L540,392 C360,410 180,425 0,438 Z" fill="var(--blue)"/>
    <path d="M0,205 C160,185 330,130 540,135 L540,378 C360,395 180,410 0,425 Z" fill="var(--green)"/>
  </svg>
  <div class="photo photo--round" style="left:352px;top:312px;width:140px;height:140px;background:linear-gradient(135deg,#5b6570,#b7bfc7 50%,#4a535c)" role="img" aria-label="Server racks in a data center aisle"></div>
  <div class="photo photo--round" style="left:284px;top:408px;width:62px;height:62px;background:linear-gradient(135deg,#d7dde2,#8a949c)" role="img" aria-label="Clean modern office meeting room"></div>

  <div class="title-block">
    <div class="kicker">COMMERCIAL</div>
    <h1>JANITORIAL SERVICE</h1>
    <p>High Tech Bio Tech Manufacturing Office Property<br>Management Company</p>
  </div>

  <div class="col" style="left:28px;top:432px;width:232px">
    <div class="h-section">GO GREEN, STAY GREEN</div>
    <p>Marlowcrest is a well-respected leader in the environmentally-preferred green cleaning industry.</p>
    <p>Marlowcrest remains at the forefront of green cleaning development, by tailoring sustainable, environmentally friendly and cost-effective programs to meet the specific demands of each of its clients.</p>
    <div class="h-sub">Marlowcrest Green cleaning program offers the following:</div>
    <ul class="checks">
      <li>Continuous improvement training for all associates</li>
      <li>Standardized sustainable cleaning processes and procedures</li>
      <li>Experienced, invested, interested, and accountable management</li>
      <li>Certified sustainable chemicals, products, tools, and equipment at competitive prices</li>
      <li>Recycling programs, duct cleaning, filter changing.</li>
    </ul>
  </div>

  <div class="col" style="left:272px;top:486px;width:250px">
    <div class="h-section">OUR FEATURES</div>
    <div class="features">
      <div class="feature"><div class="icon"><svg width="20" height="20" viewBox="0 0 20 20"><rect x="2" y="4" width="16" height="14" rx="2" fill="none" stroke="#fff" stroke-width="1.6"/><line x1="2" y1="8" x2="18" y2="8" stroke="#fff" stroke-width="1.6"/><text x="10" y="16" fill="#fff" font-size="5.5" font-family="Lato" font-weight="700" text-anchor="middle">24/7</text></svg></div>24/7<br>access</div>
      <div class="feature"><div class="icon"><svg width="20" height="20" viewBox="0 0 20 20"><rect x="2" y="4" width="16" height="14" rx="2" fill="none" stroke="#fff" stroke-width="1.6"/><line x1="2" y1="8" x2="18" y2="8" stroke="#fff" stroke-width="1.6"/><text x="10" y="16.5" fill="#fff" font-size="7" font-family="Lato" font-weight="900" text-anchor="middle">25</text></svg></div>Locally owned and operated</div>
      <div class="feature"><div class="icon"><svg width="20" height="20" viewBox="0 0 20 20" fill="none" stroke="#fff" stroke-width="1.5"><circle cx="6" cy="6" r="2.2"/><circle cx="14" cy="6" r="2.2"/><path d="M2 13c0-2.5 8-2.5 8 0M10 13c0-2.5 8-2.5 8 0"/><rect x="3" y="15" width="14" height="3"/></svg></div>Service<br>Excellence</div>
      <div class="feature"><div class="icon"><svg width="20" height="20" viewBox="0 0 20 20" fill="#fff"><circle cx="10" cy="4" r="2.5"/><path d="M6 8h8v7h-2v4h-4v-4H6z"/></svg></div>25 Years in<br>business</div>
    </div>
    <div style="display:flex;justify-content:space-between;align-items:flex-end;margin-top:16px">
      <div class="cta">CALL NOW TODAY FOR<br>INFORMATION<br><span class="phone">408-555-0182</span></div>
      <div class="brand"><span class="mark"></span><span class="name">Marlowcrest</span></div>
    </div>
  </div>

  <div class="footer">
    <span><i class="dot"></i>2240 Alder Park Way #C San Jose, CA 95131</span>
    <span><i class="dot"></i>www.marlowcrestfacilitysvc.com</span>
  </div>
</section>

<section class="sheet sheet--back">
  <div class="photo photo--cleanroom" role="img" aria-label="Bright cleanroom corridor with glass partitions"></div>
  <svg class="backdrop" viewBox="0 0 540 728" aria-hidden="true">
    <path d="M0,200 C180,215 360,190 540,160 L540,176 C360,205 180,228 0,214 Z" fill="var(--green)"/>
    <path d="M0,214 C180,228 360,205 540,176 L540,182 C360,212 180,234 0,220 Z" fill="var(--blue)"/>
  </svg>
  <div class="photo photo--round" style="left:28px;top:128px;width:138px;height:138px;background:linear-gradient(135deg,#7aa7cf,#dfe9f2 55%,#5c8fbf)" role="img" aria-label="Technician in cleanroom gown working in a lab"></div>
  <div class="photo photo--round" style="left:152px;top:192px;width:80px;height:80px;background:linear-gradient(135deg,#e8ecef,#9aa5ad)" role="img" aria-label="Laboratory equipment on a clean bench"></div>

  <div class="col" style="left:24px;top:290px;width:232px">
    <div class="h-section">SERVICES OFFERED</div>
    <div class="h-sub" style="margin-top:0">Cleaning For Every Industry</div>
    <p>Marlowcrest focuses on clients where the quality of cleaning, safety, maintenance, and appearance is critical to the basic function of the establishment. We serve a wide variety of market sectors, including the following, with our vast expertise and superior quality.</p>
    <div class="h-sub">Cleaning For Your High Tech Data Centers</div>
    <div class="lead-in">Working with the high-technology environment means flexibility and full service. A few things we offer:</div>
    <ul class="checks">
      <li>Secure hiring practices through rigorous VerityScreen background checks</li>
      <li>Site-specific training customer-customized</li>
      <li>Quick-thinking and empowered on-site staff</li>
      <li>Hands-on management oversight</li>
      <li>Inspections and quality control</li>
    </ul>
    <div class="h-sub">Contamination Control Taken Seriously</div>
    <div class="lead-in">Marlowcrest provides the following services:</div>
    <ul class="checks checks--two">
      <li>Cleanroom cleaning programs</li>
      <li>Gown Room management</li>
      <li>SOP writing</li>
      <li>Data center/ESD cleaning</li>
    </ul>
  </div>

  <div style="position:absolute;left:24px;top:620px;display:flex;align-items:flex-end;gap:16px">
    <div class="brand"><span class="mark"></span><span class="name">Marlowcrest</span></div>
    <div class="cta">CALL NOW TODAY FOR<br>INFORMATION<br><span class="phone">408-555-0182</span></div>
  </div>

  <div class="col" style="left:269px;top:236px;width:250px">
    <div class="h-sub" style="margin-top:0">Campus And Classroom Cleaning Service</div>
    <div class="lead-in">Our educational clients benefit from our services in the following manner:</div>
    <ul class="checks">
      <li>Facility services delivered on time and within budget</li>
      <li>Efficient and realistic planning, scheduling, budgeting, and cost control methods</li>
      <li>Partnering with an environmentally conscious company that cares about its clients, their employees, and their facilities</li>
      <li>Experiencing the feeling of real trust in a facility services provider dedicated to its clients and the health of their companies</li>
    </ul>
    <div class="h-section" style="margin-top:8px">WHY ARE WE BEST</div>
    <div class="h-sub" style="margin-top:0">Service Excellence</div>
    <p>With our highly-trained, in-house workforce, you can trust that we’ll provide you with services that increase efficiencies and lower your operating expenses—all while maintaining a uniform standard of service excellence.</p>
    <div class="h-sub">Breadth of Services</div>
    <p>We’ll provide you with an unrivaled range of facilities solutions that will keep your properties safe, clean, comfortable and energy efficient.</p>
    <div class="h-sub">Technology-Enabled Workforce</div>
    <p>Your facilities will be serviced with the support of innovative technology solutions that will simplify service delivery and allow for greater transparency.</p>
    <div class="h-sub">Guaranteed Sustainability Solutions</div>
    <p>We’ve got expertise to support all of your sustainability goals, including green cleaning, VORQ support, bundled energy solutions, and more.</p>
  </div>

  <div class="footer">
    <span><i class="dot"></i>2240 Alder Park Way #C San Jose, CA 95131</span>
    <span><i class="dot"></i>www.marlowcrestfacilitysvc.com</span>
  </div>
</section>

</body>
</html>
```